3D Animation for Screen on Entry Gate

We need 2 x 3D Animations for the entry screen that will sit on top of a turnstile as you enter a venue. These images need to be very clear, modern looking animated images.

1) The first animation will need to be a moving flashing or moving from small to large, Red Cross that also reads "Invalid"
2) The 2nd image needs to have the same look and feel but be a moving Green arrow - moving from the bottom of the screen to the top of the screen that also reads Access Granted

We will require the file to be provided as a mp4. thank you.

```html
<!DOCTYPE html>
<html lang="en">
<head>
<meta charset="utf-8">
<title>Entry Gate Screens – Access Granted / Invalid</title>
<link rel="stylesheet" href="https://fonts.googleapis.com/css2?family=Archivo+Black&family=Montserrat:wght@400&display=swap">
<style>
  :root{
    --stage:#000000;
    --green-light:#4f8a3a;
    --green-mid:#2f5e26;
    --green-dark:#1b3216;
    --ring-green:#1fa542;
    --ring-green-dark:#0c5a22;
    --red-light:#c8202a;
    --red-mid:#8e1218;
    --red-dark:#3e0608;
    --ring-red:#e0222b;
    --ring-red-dark:#6a0a0e;
    --label:#ffffff;
    --extrude:#5d5d5d;
  }
  html,body{margin:0;padding:0;overflow:hidden;}
  body{width:1200px;height:1200px;background:var(--stage);position:relative;}
  .screen{position:absolute;overflow:hidden;}
  .screen svg{display:block;width:100%;height:100%;}
  .screen--granted-wide{left:0;top:0;width:752px;height:422px;
    background:radial-gradient(ellipse at 58% 45%,var(--green-light) 0%,var(--green-mid) 55%,var(--green-dark) 100%);}
  .screen--granted-tall{left:764px;top:0;width:436px;height:774px;
    background:radial-gradient(ellipse at 50% 42%,var(--green-light) 0%,var(--green-mid) 45%,var(--green-dark) 100%);}
  .screen--invalid-tall{left:0;top:424px;width:436px;height:776px;
    background:radial-gradient(ellipse at 50% 52%,var(--red-light) 0%,var(--red-mid) 45%,var(--red-dark) 100%);}
  .screen--invalid-wide{left:448px;top:776px;width:752px;height:424px;
    background:radial-gradient(ellipse at 45% 45%,var(--red-light) 0%,var(--red-mid) 50%,var(--red-dark) 100%);}
  .format-label{font-family:"Montserrat",sans-serif;font-size:21px;fill:var(--label);}
  .headline{font-family:"Archivo Black",sans-serif;}
  .headline--extrude{fill:var(--extrude);}
  .headline--face{fill:url(#silver);}
</style>
</head>
<body>

<svg width="0" height="0" style="position:absolute" aria-hidden="true">
  <defs>
    <linearGradient id="silver" x1="0" y1="0" x2="0" y2="1">
      <stop offset="0" stop-color="#ffffff"/>
      <stop offset="0.55" stop-color="#d9d9d9"/>
      <stop offset="1" stop-color="#9a9a9a"/>
    </linearGradient>
    <linearGradient id="ring-green-grad" x1="0" y1="0" x2="1" y2="1">
      <stop offset="0" stop-color="#2ccf5a"/>
      <stop offset="1" stop-color="var(--ring-green)"/>
    </linearGradient>
    <radialGradient id="disc-red-grad" cx="0.6" cy="0.6" r="0.7">
      <stop offset="0" stop-color="#ff3a40"/>
      <stop offset="1" stop-color="#a5141a"/>
    </radialGradient>
    <g id="tick-icon">
      <circle cx="10" cy="8" r="92" fill="none" stroke="var(--ring-green-dark)" stroke-width="24"/>
      <circle cx="0" cy="0" r="90" fill="none" stroke="url(#ring-green-grad)" stroke-width="22"/>
      <polygon points="-70,-2 -52,-16 4,44 196,-180 204,-172 4,80" fill="url(#silver)"/>
    </g>
    <g id="cross-icon">
      <circle cx="12" cy="6" r="100" fill="var(--ring-red-dark)"/>
      <circle cx="0" cy="0" r="100" fill="url(#disc-red-grad)"/>
      <circle cx="0" cy="0" r="86" fill="none" stroke="#b5161d" stroke-width="6"/>
      <g fill="url(#silver)">
        <rect x="-72" y="-22" width="144" height="44" transform="rotate(45)"/>
        <rect x="-72" y="-22" width="144" height="44" transform="rotate(-45)"/>
      </g>
    </g>
  </defs>
</svg>

<section class="screen screen--granted-wide">
  <svg viewBox="0 0 752 422">
    <text class="format-label" x="724" y="45" text-anchor="end">1280x720 Format</text>
    <use href="#tick-icon" transform="translate(160 232) scale(1.02)"/>
    <g class="headline" font-size="88">
      <text class="headline--extrude" x="298" y="236" textLength="360" lengthAdjust="spacingAndGlyphs">ACCESS</text>
      <text class="headline--face" x="292" y="232" textLength="360" lengthAdjust="spacingAndGlyphs">ACCESS</text>
      <text class="headline--extrude" x="298" y="318" textLength="413" lengthAdjust="spacingAndGlyphs">GRANTED</text>
      <text class="headline--face" x="292" y="314" textLength="413" lengthAdjust="spacingAndGlyphs">GRANTED</text>
    </g>
  </svg>
</section>

<section class="screen screen--granted-tall">
  <svg viewBox="0 0 436 774">
    <text class="format-label" x="422" y="40" text-anchor="end">720 x 1280 Format</text>
    <use href="#tick-icon" transform="translate(204 264) scale(0.92)"/>
    <g class="headline" font-size="88">
      <text class="headline--extrude" x="54" y="484" textLength="336" lengthAdjust="spacingAndGlyphs">ACCESS</text>
      <text class="headline--face" x="48" y="480" textLength="336" lengthAdjust="spacingAndGlyphs">ACCESS</text>
      <text class="headline--extrude" x="30" y="574" textLength="388" lengthAdjust="spacingAndGlyphs">GRANTED</text>
      <text class="headline--face" x="24" y="570" textLength="388" lengthAdjust="spacingAndGlyphs">GRANTED</text>
    </g>
  </svg>
</section>

<section class="screen screen--invalid-tall">
  <svg viewBox="0 0 436 776">
    <text class="format-label" x="422" y="46" text-anchor="end">720 x 1280 Format</text>
    <use href="#cross-icon" transform="translate(216 292) scale(1.04)"/>
    <g class="headline" font-size="100">
      <text class="headline--extrude" x="38" y="506" textLength="372" lengthAdjust="spacingAndGlyphs">INVALID</text>
      <text class="headline--face" x="32" y="502" textLength="372" lengthAdjust="spacingAndGlyphs">INVALID</text>
    </g>
  </svg>
</section>

<section class="screen screen--invalid-wide">
  <svg viewBox="0 0 752 424">
    <text class="format-label" x="726" y="52" text-anchor="end">1280x720 Format</text>
    <use href="#cross-icon" transform="translate(160 224) scale(0.92 1.08)"/>
    <g class="headline" font-size="94">
      <text class="headline--extrude" x="294" y="258" textLength="380" lengthAdjust="spacingAndGlyphs">INVALID</text>
      <text class="headline--face" x="288" y="254" textLength="380" lengthAdjust="spacingAndGlyphs">INVALID</text>
    </g>
  </svg>
</section>

</body>
</html>
```